Flyer für Verkauf von Radondetektoren
Zielgruppe
Ich verkaufe Radondetektoren zur Messung von Radon in Innenräumen. Zielgruppe sind Privatpersonen, Firmen, Genossenschaften und andere Hauseigentümer.
Aufgabenstellung
Ich brauche das Design für meine Messanleitung.
Kreativ - modern - weniger kann mehr sein
Struktur ist wichtigt, es soll also einfach sein zu lesen und zu verstehen, was gemacht werden soll. Können Bulletpoints, Icons mit eingebracht werden.
Wichtig ist auch, dass die beiden Logos 'Luftprüfer.de' und KALTMARK' auf der Messanleitung vorhanden sind. Wobei 'Luftprüfer.de' das Hauptlogo ist.
DIN format dachte ich A4 beidseitig (Text müsste also auf diese Grösse angepasst werden).
Kann natürlich auch Flyer-Format sein oder andere Vorschläge!
Bildmaterial gibt es auf unsere Homepage https://luftprüfer.de und https://luftkollen.se . Diese haben wir bereits gekauft und können verwendet werden. Ich lade sie den bei Bedarf hoch. Es können natürlich auch andere Vorschläge kommen.

```html
<!DOCTYPE html>
<html lang="de">
<head>
<meta charset="utf-8">
<title>Messanleitung – Luftprüfer.de</title>
<link href="https://fonts.googleapis.com/css2?family=Roboto:wght@400;500;700&family=Roboto+Condensed:wght@700&display=swap" rel="stylesheet">
<style>
  :root {
    --coral: #e8575a;
    --coral-soft: rgba(232, 87, 90, 0.82);
    --photo-warm: #d9c7b8;
    --photo-cool: #c9d3da;
    --ink: #222222;
    --body: #3a3a3a;
    --accent-yellow: #f2c319;
    --paper: #ffffff;
    --backdrop: #e9e7e4;
  }
  * { box-sizing: border-box; margin: 0; padding: 0; }
  html, body { width: 1200px; height: 800px; overflow: hidden; }
  body {
    background: var(--backdrop);
    font-family: "Roboto", Arial, sans-serif;
    color: var(--body);
  }
  .spread {
    position: absolute; left: 30px; top: 20px;
    width: 1140px; height: 760px;
    display: flex;
    box-shadow: 0 6px 24px rgba(0,0,0,0.18);
  }
  .page {
    position: relative; width: 570px; height: 760px;
    background: var(--paper); overflow: hidden;
  }
  .page--left { border-right: 1px solid #e2e2e2; }
  .page-header { position: relative; height: 170px; }
  .header-photo { position: absolute; inset: 0; }
  .page--left .header-photo { background: linear-gradient(100deg, var(--photo-cool) 0%, var(--photo-warm) 45%, #e7b7a8 100%); }
  .page--right .header-photo { background: linear-gradient(100deg, #b9c2c9 0%, #d8d4cf 40%, #d9a79b 100%); }
  .brand-panel {
    position: absolute; top: 0; right: 0; bottom: 0; width: 62%;
    background: var(--coral-soft);
    border-bottom-left-radius: 18px;
    display: flex; flex-direction: column; justify-content: flex-end;
    padding: 0 0 22px 60px;
  }
  .brand-name {
    font-family: "Roboto Condensed", Arial, sans-serif;
    font-weight: 700; font-size: 30px; color: #fff; line-height: 1;
  }
  .brand-tagline { font-size: 10px; color: #fff; margin-top: 3px; }
  .page-body { padding: 18px 34px 0 34px; }
  .section-title {
    display: flex; align-items: center; gap: 10px;
    font-family: "Roboto Condensed", Arial, sans-serif;
    font-weight: 700; color: var(--ink); font-size: 15px; line-height: 1.2;
    margin: 10px 0 6px;
  }
  .section-icon {
    flex: 0 0 auto; width: 22px; height: 22px; border-radius: 4px;
    background: var(--coral);
  }
  .section-title--accent { color: var(--coral); font-size: 14px; }
  .step-title {
    display: flex; align-items: flex-start; gap: 10px;
    font-family: "Roboto Condensed", Arial, sans-serif;
    font-weight: 700; color: var(--ink); font-size: 19px; line-height: 1.15;
    text-transform: uppercase; margin: 16px 0 8px;
  }
  .sub-title { font-weight: 700; color: var(--ink); font-size: 13px; margin: 10px 0 4px; }
  p, li { font-size: 10.5px; line-height: 1.45; }
  ul.bullets { list-style: none; }
  ul.bullets li { position: relative; padding-left: 14px; margin-bottom: 2px; }
  ul.bullets li::before {
    content: ""; position: absolute; left: 0; top: 4px;
    border-left: 7px solid var(--accent-yellow);
    border-top: 4px solid transparent; border-bottom: 4px solid transparent;
  }
  .address { display: flex; gap: 10px; align-items: center; margin: 10px 0; }
  .address strong { display: block; font-size: 11px; color: var(--ink); line-height: 1.5; }
  a { color: var(--ink); }
</style>
</head>
<body>
<main class="spread">

  <section class="page page--left">
    <header class="page-header">
      <div class="header-photo" role="img" aria-label="Foto: Paar entspannt auf dem Sofa im hellen Wohnzimmer"></div>
      <div class="brand-panel">
        <div class="brand-name">Luftprüfer.de</div>
        <div class="brand-tagline">Saubere Luft, klare Werte</div>
      </div>
    </header>
    <div class="page-body">
      <h2 class="section-title">
        <span class="section-icon" aria-hidden="true"></span>
        Radonmessungen für Mehrfamilienhäuser, Wohnungen und Wohnkomplexen:
      </h2>
      <ul class="bullets">
        <li>Alle Wohnungen mit direktem Bodenkontakt sowie mindestens eine Wohnung pro Etage sollten gemessen werden. Wählen Sie dabei Wohnungen, die an Aufzügen oder Luftschächten liegen.</li>
        <li>In größeren Wohnkomplexen sollten insgesamt mindestens 20% aller Wohnungen in einem Gebäude gemessen werden.</li>
        <li>Es sollten mindestens zwei Wohnräume pro ausgewählte Wohnung gemessen werden. Wählen Sie Räume aus, in denen Sie sich oft aufhalten (z.B. das Wohn- und Schlafzimmer). Vermeiden Sie aber Räume, in denen das Fenster mehrere Stunden am Tag oder in der Nacht geöffnet ist.</li>
        <li>Selbst bei einer Einzimmerwohnung sollten Sie zwei Detektoren aufstellen.</li>
      </ul>
      <h2 class="section-title">Radonmessungen für Arbeitsplätze und öffentliche Gebäude:</h2>
      <ul class="bullets">
        <li>Wählen Sie Räume, die regelmäßig mehr als vier Stunden pro Tag genutzt werden.</li>
        <li>Messen Sie alle unterirdischen Räumlichkeiten, da hier meist das größte Risiko einer erhöhten Radonkonzentration erwartet wird.</li>
        <li>Messen Sie alle Räume im Erdgeschoß. Für größere Räumlichkeiten empfehlen wir einen Detektor pro 200 m².</li>
        <li>In den oberen Etagen sollten Sie mit mindestens zwei Detektoren, sowie mindestens einem Detektor pro 200 m² messen.</li>
        <li>Falls Ihr Arbeitsplatz in einem Radon-Vorsorgegebiet liegt und somit der Messpflicht unterliegt, muss die Messdauer von 12 Monaten eingehalten werden.</li>
      </ul>
      <h3 class="section-title section-title--accent">Platzierung der Detektoren im Raum:</h3>
      <ul class="bullets">
        <li>Platzieren Sie die Detektoren in einem Mindestabstand von 20 cm zu Wänden, 50 cm zu Abluftventilen, sowie 1,50 m zu Fenstern, Außentüren, Zuluftsventilen und Heizkörpern.</li>
        <li>Stellen Sie die Detektoren nicht auf dem Boden, an starken Wärmequellen oder Luftströmen auf. Vermeiden Sie auch Räume mit hoher Luftfeuchtigkeit, wie zum Beispiel das Badezimmer.</li>
        <li>Die Detektoren können entweder stehend (auf einem Tisch, im Regal oder einer Schrankwand) oder hängend mitten im Raum (z.B. von einer Lampe) platziert werden.</li>
        <li>Stellen Sie die Detektoren während der gesamten Messdauer nicht um.</li>
      </ul>
    </div>
  </section>

  <section class="page page--right">
    <header class="page-header">
      <div class="header-photo" role="img" aria-label="Foto: Team bespricht sich an einem Schreibtisch im Büro"></div>
      <div class="brand-panel">
        <div class="brand-name">Luftprüfer.de</div>
        <div class="brand-tagline">Saubere Luft, klare Werte</div>
      </div>
    </header>
    <div class="page-body">
      <ul class="bullets">
        <li>Versuchen Sie nicht das Gehäuse der Detektoren zu öffnen und platzieren Sie diese immer außer Reichweite von Kindern.</li>
      </ul>
      <h2 class="step-title">
        <svg width="26" height="24" viewBox="0 0 26 24" aria-hidden="true"><circle cx="11" cy="13" r="9" fill="none" stroke="var(--accent-yellow)" stroke-width="2.5"/><path d="M6 12 L11 17 L24 3" fill="none" stroke="var(--accent-yellow)" stroke-width="3" stroke-linecap="round"/></svg>
        Schritt 3: Radonmessung
      </h2>
      <p>Die Radonmessung beginnt, sobald Sie die radondichten Verpackungen öffnen. Bitte halten Sie die Messdauer wie folgt ein:</p>
      <h3 class="sub-title">Kurzzeitmessung:</h3>
      <ul class="bullets">
        <li>Mindestmessdauer 10 Tage (bis hin zu 30 Tagen).</li>
        <li>Führen Sie die Messung vorzugsweise in der Heizperiode (1. Oktober – 30. April) durch.</li>
        <li>Kurzzeitmessungen werden oft beim Kauf oder Verkauf von Immobilien genutzt, um ein mögliches Gefährdungspotential abschätzen zu können, oder wenn die Zeit nicht ausreicht, um eine Langzeitmessung durchzuführen.</li>
      </ul>
      <h3 class="sub-title">Langzeitmessung:</h3>
      <ul class="bullets">
        <li>Mindestmessdauer 3 Monate während der Heizperiode (1. Oktober – 30. April).</li>
        <li>Um einen Jahresmittelwert der Radonkonzentration in Innenräumen ermitteln zu können, halten Sie die Messdauer von 12 Monaten ein.</li>
        <li>Falls Ihr Arbeitsplatz in einem Radon-Vorsorgegebiet liegt und somit der Messpflicht unterliegt, muss die Messdauer von 12 Monaten eingehalten werden.</li>
      </ul>
      <h2 class="step-title">
        <svg width="26" height="24" viewBox="0 0 26 24" aria-hidden="true"><circle cx="11" cy="13" r="9" fill="none" stroke="var(--accent-yellow)" stroke-width="2.5"/><path d="M6 12 L11 17 L24 3" fill="none" stroke="var(--accent-yellow)" stroke-width="3" stroke-linecap="round"/></svg>
        Schritt 4: Abschluss der Radonmessung<br>mit abschließendem Prüfbericht
      </h2>
      <p>Nach Ablauf der Messdauer, loggen Sie sich auf <a href="https://kundenportal.kaltmark.se/de">https://kundenportal.kaltmark.se/de</a> in Ihrem Account ein. Vermerken Sie hier das Ende der Messung und senden Sie anschließend alle Radondetektoren ausreichend frankiert in einem Umschlag oder einem Karton zeitnah an unsere Rücksendeadresse:</p>
      <div class="address">
        <svg width="22" height="30" viewBox="0 0 22 30" aria-hidden="true"><path d="M11 1 C5 1 1 5.5 1 11 C1 18 11 29 11 29 C11 29 21 18 21 11 C21 5.5 17 1 11 1 Z" fill="var(--coral)"/><circle cx="11" cy="11" r="4" fill="#fff"/></svg>
        <div><strong>Luftprüfer.de</strong><strong>Lindenstieg 14 – 21337 Birkenau-Nord – Deutschland</strong></div>
      </div>
      <p>Sobald die Radondetektoren im Labor von Kaltmark eingetroffen sind, werden diese fachgerecht analysiert und die Ergebnisse der Radonmessung ausgewertet. Ein vollständiger Prüfbericht wird Ihnen innerhalb 36 Stunden nach Erhalt der Detektoren im Labor per E-Mail zugeschickt.</p>
    </div>
  </section>

</main>
</body>
</html>
```